Die Designerin hat meine Vorstellungen am besten verstanden und umgesetzt. Sie war mir gegenüber sehr verständnisvoll und entgegenkommend. Die Kommunikation mit ihr war sehr erfreulich und sympathisch. Bei meinem nächsten Projekt werde ich mich zuerst an sie wenden.

```html
<!DOCTYPE html>
<html lang="de">
<head>
<meta charset="utf-8">
<title>Mein verrückter Sommer in Brandholm – Buchcover</title>
<link rel="stylesheet" href="https://fonts.googleapis.com/css2?family=Amatic+SC:wght@700&family=Source+Serif+4:opsz,wght@8..60,700&display=swap">
<style>
  :root {
    --backdrop: #d63a33;
    --cover-orange: #f0a02a;
    --cover-orange-light: #f3b04a;
    --cover-orange-deep: #ea8a24;
    --accent-red: #d81f26;
    --scooter-red: #e8401f;
    --title-white: #ffffff;
  }
  * { margin: 0; padding: 0; box-sizing: border-box; }
  html, body {
    width: 1200px;
    height: 1055px;
    overflow: hidden;
    background: var(--backdrop);
  }
  .canvas {
    position: relative;
    width: 1200px;
    height: 1055px;
  }
  .book-cover {
    position: absolute;
    left: 264px;
    top: 27px;
    width: 671px;
    height: 1000px;
    background: radial-gradient(ellipse at 50% 40%, var(--cover-orange-light) 0%, var(--cover-orange) 55%, var(--cover-orange-deep) 100%);
    box-shadow: 0 4px 14px rgba(0, 0, 0, 0.18);
    overflow: hidden;
  }
  .cover-illustration {
    position: absolute;
    left: 60px;
    top: 330px;
    width: 560px;
    height: 670px;
  }
  .genre-label {
    position: absolute;
    top: 8px;
    width: 100%;
    text-align: center;
    font-family: "Source Serif 4", Georgia, serif;
    font-weight: 700;
    font-size: 27px;
    color: var(--accent-red);
    letter-spacing: 0.5px;
  }
  .book-title { font-weight: 700; }
  .title-line {
    position: absolute;
    width: 100%;
    text-align: center;
    font-family: "Amatic SC", "Arial Narrow", sans-serif;
    font-weight: 700;
    font-size: 54px;
    line-height: 1;
    color: var(--title-white);
    letter-spacing: 24px;
    padding-left: 24px;
    white-space: nowrap;
  }
  .title-line--1 { top: 92px; }
  .title-line--2 { top: 244px; }
  .title-line--3 { top: 395px; letter-spacing: 28px; padding-left: 28px; }
  .title-line--4 { top: 547px; }
  .title-line--5 { top: 698px; }
  .author-name {
    position: absolute;
    top: 914px;
    width: 100%;
    text-align: center;
    font-family: "Source Serif 4", Georgia, serif;
    font-weight: 700;
    font-size: 28px;
    color: var(--accent-red);
    letter-spacing: 9px;
    padding-left: 9px;
    white-space: nowrap;
  }
</style>
</head>
<body>
<main class="canvas">
  <section class="book-cover">
    <svg class="cover-illustration" viewBox="0 0 560 670" role="img" aria-label="Illustration eines roten Motorrollers im Retro-Stil mit langen orangefarbenen Schatten">
      <defs>
        <radialGradient id="scooter-tone" cx="48%" cy="38%" r="50%">
          <stop offset="0%" stop-color="#e8401f" stop-opacity="0.8"/>
          <stop offset="55%" stop-color="#ec5a22" stop-opacity="0.4"/>
          <stop offset="100%" stop-color="#f0a02a" stop-opacity="0"/>
        </radialGradient>
        <linearGradient id="shadow-tone" x1="0" y1="0" x2="0" y2="1">
          <stop offset="0%" stop-color="#ee6a22" stop-opacity="0"/>
          <stop offset="100%" stop-color="#ee6a22" stop-opacity="0.45"/>
        </linearGradient>
      </defs>
      <rect width="560" height="670" fill="url(#scooter-tone)"/>
      <rect y="470" width="560" height="200" fill="url(#shadow-tone)"/>
    </svg>

    <p class="genre-label">ROMAN</p>

    <h1 class="book-title">
      <span class="title-line title-line--1">MEIN</span>
      <span class="title-line title-line--2">VERRÜCKTER</span>
      <span class="title-line title-line--3">SOMMER</span>
      <span class="title-line title-line--4">IN</span>
      <span class="title-line title-line--5">BRANDHOLM</span>
    </h1>

    <p class="author-name">BERNHARD KOLWITZ</p>
  </section>
</main>
</body>
</html>
```